New Plumbing Company

We are looking for a smart and creative business card design for our new plumbing company. We are looking for creativity and originality in our business cards.

Industry/Entity Type

Plumbing

Contact Information for Business Card

Crestline Plumbing
Peter Halvane
Managing Director
Telephone Number : 0481529604
Email : service@crestlineplumbing.com.au
Website : www.crestlineplumbing.com.au
Lic. 508264K

Colors
0692cd
33a6d7
000000

Requirements
Must have
• I want the business card to be designed on a black background using the blue tones i have selected as seen in the company logo.

```html
<!DOCTYPE html>
<html lang="en">
<head>
<meta charset="utf-8">
<title>Crestline Plumbing – Business Card</title>
<link rel="stylesheet" href="https://fonts.googleapis.com/css2?family=Roboto:wght@300;400;500;700&display=swap">
<style>
  :root {
    --stage: #e4e4e4;
    --blue: #0692cd;
    --blue-light: #33a6d7;
    --black: #000000;
    --white: #ffffff;
  }
  * { margin: 0; padding: 0; box-sizing: border-box; }
  html, body {
    width: 1200px; height: 1199px; overflow: hidden;
    background: var(--stage);
    font-family: "Roboto", Arial, sans-serif;
  }
  .card {
    position: absolute; left: 170px; width: 842px; height: 481px;
    border-radius: 26px; overflow: hidden;
    background: var(--blue);
  }
  .card--front { top: 73px; }
  .card--back { top: 619px; }
  .card__shape { position: absolute; inset: 0; width: 100%; height: 100%; }
  .card__shape path { fill: var(--black); }

  .person { position: absolute; left: 62px; top: 206px; color: var(--white); }
  .person__name { font-weight: 500; font-size: 31px; letter-spacing: 0.2px; }
  .person__title { font-weight: 300; font-size: 25px; margin-top: 8px; }
  .licence {
    position: absolute; left: 72px; top: 422px;
    color: var(--white); font-weight: 300; font-size: 24px;
  }

  .contact { position: absolute; left: 358px; top: 212px; color: var(--white); }
  .contact__row { display: flex; align-items: center; height: 39px; font-weight: 300; font-size: 25px; }
  .contact__icon { width: 48px; display: flex; justify-content: center; }
  .contact__icon svg { display: block; }

  .brand {
    position: absolute; left: 308px; top: 192px;
    display: flex; align-items: center; gap: 22px;
  }
  .brand__circle {
    width: 92px; height: 92px; border-radius: 50%;
    border: 4px solid var(--blue);
  }
  .brand__name {
    color: var(--white); font-weight: 300; font-size: 38px; white-space: nowrap;
  }
  .website {
    position: absolute; left: 311px; top: 408px;
    color: var(--blue-light); font-weight: 300; font-size: 30px;
  }
</style>
</head>
<body>

<section class="card card--front">
  <svg class="card__shape" viewBox="0 0 842 481" preserveAspectRatio="none" aria-hidden="true">
    <path d="M508 0 L384 124 C340 170 318 225 318 288 C318 370 360 435 420 481 L842 481 L842 0 Z"/>
  </svg>

  <div class="person">
    <div class="person__name">Peter Halvane</div>
    <div class="person__title">Managing Director</div>
  </div>
  <div class="licence">Lic. 508264K</div>

  <div class="contact">
    <div class="contact__row">
      <span class="contact__icon">
        <svg width="18" height="26" viewBox="0 0 18 26" aria-hidden="true">
          <rect x="1" y="1" width="16" height="24" rx="1.5" fill="none" stroke="#fff" stroke-width="1.6"/>
          <rect x="4" y="4" width="10" height="6" fill="none" stroke="#fff" stroke-width="1.2"/>
          <path d="M4 14h10M4 17h10M4 20h10M7.3 13v9M10.7 13v9" stroke="#fff" stroke-width="1"/>
        </svg>
      </span>
      <span>0481529604</span>
    </div>
    <div class="contact__row">
      <span class="contact__icon">
        <svg width="30" height="20" viewBox="0 0 30 20" aria-hidden="true">
          <rect x="0" y="0" width="30" height="20" fill="#fff"/>
          <path d="M1 1 L15 12 L29 1" fill="none" stroke="#000" stroke-width="2.4"/>
        </svg>
      </span>
      <span>service@crestlineplumbing.com.au</span>
    </div>
  </div>
</section>

<section class="card card--back">
  <svg class="card__shape" viewBox="0 0 842 481" preserveAspectRatio="none" aria-hidden="true">
    <path d="M325 0 L199 124 C158 170 135 225 135 288 C135 370 175 435 238 481 L842 481 L842 0 Z"/>
  </svg>

  <div class="brand">
    <span class="brand__circle"></span>
    <span class="brand__name">Crestline Plumbing</span>
  </div>
  <div class="website">www.crestlineplumbing.com.au</div>
</section>

</body>
</html>
```